Skincare Cleanser Bottle Label

New product launch of a mint facial cleanser.
Brand is called Dorvelle.
Product will be called Lunara.
Looking for a label design that can be printed using silk screening.
High gloss white plastic bottle. 8oz. White push pump top.
Clinical skincare brand, professional image, sold in medical spas.

Target Market(s)

Women Age 20-65

Industry/Entity Type

Health And Wellness

Font styles to use
Serif
Sans Serif

Requirements
Must have
• Dorvelle brand name in the orignal font.
Should not have
• Multiple colours.

```html
<!DOCTYPE html>
<html lang="en">
<head>
<meta charset="utf-8">
<title>Dorvelle Lunara – Mint Facial Cleanser Label</title>
<link rel="stylesheet" href="https://fonts.googleapis.com/css2?family=Josefin+Sans:wght@300;400;600&family=Roboto+Slab:wght@300&display=swap">
<style>
  :root {
    --page: #f1f1f1;
    --label: #ffffff;
    --ink: #1a1a1a;
    --ink-soft: #444444;
    --panel-grey: #6a6a6a;
    --band-black: #141414;
    --paper-white: #ffffff;
  }
  * { margin: 0; padding: 0; box-sizing: border-box; }
  html, body {
    width: 1200px;
    height: 1200px;
    overflow: hidden;
    background: var(--page);
  }
  .label {
    position: absolute;
    left: 376px;
    top: 68px;
    width: 448px;
    height: 1064px;
    background: var(--label);
    font-family: "Josefin Sans", sans-serif;
    color: var(--ink);
  }
  .brand-name {
    position: absolute;
    left: 8px;
    top: 329px;
    transform-origin: 0 0;
    transform: rotate(-90deg);
    font-weight: 400;
    font-size: 56px;
    line-height: 52px;
    color: var(--ink);
    white-space: nowrap;
  }
  .product-panel {
    position: absolute;
    left: 60px;
    top: 7px;
    width: 360px;
    height: 270px;
    background: var(--panel-grey);
  }
  .product-name {
    position: absolute;
    right: 12px;
    bottom: 8px;
    font-family: "Roboto Slab", serif;
    font-weight: 300;
    font-size: 66px;
    line-height: 1;
    color: var(--paper-white);
    letter-spacing: 1px;
  }
  .product-type {
    position: absolute;
    left: 60px;
    top: 292px;
    width: 360px;
    font-weight: 300;
    font-size: 33px;
    color: var(--ink-soft);
    white-space: nowrap;
  }
  .claims {
    position: absolute;
    left: 60px;
    top: 393px;
    width: 330px;
    list-style: none;
    text-align: center;
    font-weight: 300;
    font-size: 26px;
    line-height: 32px;
    color: var(--ink-soft);
  }
  .promise-band {
    position: absolute;
    left: 60px;
    top: 518px;
    width: 360px;
    height: 378px;
    background: linear-gradient(to bottom, var(--band-black) 0%, var(--band-black) 32%, #2b2b2b 55%, #9a9a9a 82%, var(--paper-white) 100%);
  }
  .promise-text {
    position: absolute;
    left: 0;
    top: 30px;
    width: 100%;
    text-align: center;
    font-weight: 600;
    font-size: 14px;
    line-height: 22px;
    letter-spacing: 1.2px;
    color: var(--paper-white);
  }
  .volume {
    position: absolute;
    left: 0;
    top: 1010px;
    width: 448px;
    text-align: center;
    font-weight: 400;
    font-size: 22px;
    letter-spacing: 1px;
    color: var(--ink);
  }
</style>
</head>
<body>
  <main class="label">
    <div class="brand-name">dorvelle</div>

    <section class="product-panel">
      <h1 class="product-name">LUNARA</h1>
    </section>
    <p class="product-type">mint facial cleanser</p>

    <ul class="claims">
      <li>paraben free</li>
      <li>no preservatives</li>
      <li>no fillers</li>
    </ul>

    <section class="promise-band" role="img" aria-label="Black band fading to white through a dotted halftone texture">
      <p class="promise-text">transform the appearance<br>and health of your skin</p>
    </section>

    <p class="volume">8 oz / 235 ml</p>
  </main>
</body>
</html>
```